Brellow Publishing

I made a website myself www.brellowpublishing.co.uk a few years ago but I need a new design, which I will code. One that I can be proud of, that 's sexy, to win new customers and showcase my publishing skills. This is a publishing website so I want the home page and books page to be fantastic. I have a logo already so will like the same colour scheme or thereabouts. I have current files and features that I would like to add to your creativity and experience.

Target Market(s)

Web Designers, Graphic Designers

Industry/Entity Type

Book Publisher

Number of Pages Required

5+ page

Font styles to use
Sans Serif

Colors
0255a3
ffffff
ec1f27

Requirements
Must have
• Menu and Sub Menu
• Footer
• Buy Page - Shopping Cart
• Upload feature on the submissions page
• video section on home page (how we publish books)
• Ad space section
Nice to have
• social media bar
• Zoom in page

```html
<!DOCTYPE html>
<html lang="en">
<head>
<meta charset="utf-8">
<title>Brellow Publishing — Self-publishing that works</title>
<link href="https://fonts.googleapis.com/css2?family=Roboto:wght@400;500;700&display=swap" rel="stylesheet">
<style>
:root{
  --blue:#0255a3;
  --red:#ec1f27;
  --navy:#1d2b5a;
  --ink:#2a2a2a;
  --muted:#6b6b6b;
  --white:#ffffff;
  --band:#f4f4f4;
  --footer:#e9e9e9;
  --rule:#d6d6d6;
  --ring:#cfcfcf;
}
*{box-sizing:border-box;margin:0;padding:0}
html,body{width:1200px;height:3030px;overflow:hidden;background:var(--white)}
body{font-family:'Roboto',Arial,sans-serif;color:var(--ink);position:relative}

.site-header{height:86px;position:relative;background:var(--white)}
.brand{position:absolute;left:96px;top:26px;display:flex;align-items:center;gap:10px}
.brand-dot{width:30px;height:30px;border-radius:50%;background:var(--red)}
.brand-name{font-weight:700;font-size:20px;color:var(--navy)}
.main-nav{position:absolute;right:96px;top:35px;display:flex;gap:38px;font-size:13px;font-weight:500;color:#333}
.main-nav .active{color:var(--red)}

.hero{height:566px;position:relative;background:linear-gradient(100deg,#d9d2c9 0%,#ece8e3 40%,#b8b3ad 70%,#7a5c45 100%)}
.hero-title{position:absolute;left:95px;top:86px;font-size:37px;line-height:58px;font-weight:700;color:var(--navy)}
.hero-btn{position:absolute;left:95px;top:216px;width:134px;height:40px;border:1.5px solid var(--red);color:var(--red);font-size:13px;font-weight:700;display:flex;align-items:center;justify-content:center}
.hero-dots{position:absolute;left:578px;top:512px;display:flex;gap:6px}
.hero-dots span{width:10px;height:10px;border-radius:50%;background:var(--white)}
.hero-dots span:first-child{background:#222}

.intro{height:477px;text-align:center;position:relative}
.intro h2{padding-top:68px;font-size:25px;font-weight:500;color:var(--navy)}
.intro p{width:710px;margin:16px auto 0;font-size:14px;line-height:26px;color:var(--muted)}
.feature-row{position:absolute;top:197px;left:0;width:100%}
.feature{position:absolute;width:220px;text-align:center}
.feature-icon{width:163px;height:163px;border-radius:50%;margin:0 auto;border:4px solid var(--ring);display:flex;align-items:center;justify-content:center}
.feature-icon.red{background:var(--red)}
.feature-icon.blue{background:var(--blue)}
.feature h3{margin-top:14px;font-size:25px;font-weight:700;color:var(--navy)}

.video-band{height:301px;position:relative;background:linear-gradient(90deg,#2b2b2b,#3c3b39 40%,#2a2624 70%,#47322b);text-align:center}
.video-band h2{padding-top:92px;font-size:35px;font-weight:500;color:var(--white)}
.play{display:block;margin:16px auto 0}

.steps{height:657px;position:relative}
.section-title{display:flex;align-items:center;justify-content:center;gap:30px;font-size:25px;font-weight:500;color:var(--ink)}
.section-title::before,.section-title::after{content:"";height:1px;width:200px;background:var(--rule)}
.steps .section-title{padding-top:70px}
.step{position:absolute;width:440px;text-align:center}
.step svg{display:block;margin:0 auto}
.step h3{margin-top:12px;font-size:18px;font-weight:500;color:var(--ink)}
.step p{width:390px;margin:6px auto 0;font-size:12.5px;line-height:20px;color:var(--muted)}

.partners{height:270px;background:var(--band);position:relative}
.partners .section-title{padding-top:50px}
.partner-row{position:absolute;top:130px;left:0;width:100%;display:flex;justify-content:center;gap:20px;align-items:center;height:80px}
.partner-badge{display:block;width:136px;background:var(--white);border:1px solid #dcdcdc;border-radius:4px;position:relative}
.partner-badge::after{content:"";position:absolute;left:22px;right:22px;top:50%;height:14px;margin-top:-7px;border-radius:7px;background:var(--tone)}
.partner-badge.flat{background:transparent;border:0}
.partner-badge.flat::after{left:6px;right:6px}

.testimonials{height:370px;text-align:center;position:relative}
.testimonials .section-title{padding-top:60px}
.quote-mark{position:absolute;left:515px;top:150px;width:110px;height:110px;border-radius:50%;background:#e6e6e6}
.quote-mark span{position:absolute;left:22px;top:26px;font-size:40px;font-weight:700;color:#666}
.avatar{position:absolute;left:573px;top:140px;width:116px;height:116px;border-radius:50%;background:radial-gradient(circle at 50% 45%,#c9a58c,#6d5a4a 60%,#3e4d3a)}
.testimonials p{position:absolute;top:282px;left:0;width:100%;font-size:13.5px;line-height:22px;color:var(--muted)}

.site-footer{height:372px;background:var(--footer);position:relative}
.footer-brand{position:absolute;left:100px;top:48px;width:120px;text-align:center}
.footer-brand .brand-dot{width:46px;height:46px;margin:0 auto 10px}
.footer-brand .brand-name{font-size:16px;line-height:19px}
.footer-col{position:absolute;top:46px}
.footer-col h4{font-size:18px;font-weight:500;color:var(--ink);margin-bottom:12px}
.footer-col li{list-style:none;font-size:13.5px;color:#555;line-height:28px}
.footer-col li::before{content:"»";margin-right:8px}
.social{display:flex;gap:12px;margin-top:4px}
.social span{width:32px;height:32px;border:1px solid #9a9a9a;background:var(--white)}
.footer-rule{position:absolute;left:56px;right:56px;top:228px;height:1px;background:var(--rule)}
.copyright{position:absolute;top:248px;width:100%;text-align:center;font-size:13px;color:#666}
</style>
</head>
<body>
<header class="site-header">
  <div class="brand"><span class="brand-dot"></span><span class="brand-name">Brellow Publishing</span></div>
  <nav class="main-nav">
    <span class="active">HOME</span><span>PUBLISHING</span><span>SUBMISSIONS</span><span>BOOKS</span><span>AUTHORS</span><span>SEMINARS</span><span>CONTACT</span>
  </nav>
</header>

<section class="hero" role="img" aria-label="Photo of a smiling woman typing on a laptop">
  <h1 class="hero-title">BRELLOW PUBLISHING<br>SELF-PUBLISHING THAT WORKS</h1>
  <span class="hero-btn">SUBMIT BOOK</span>
  <div class="hero-dots"><span></span><span></span><span></span></div>
</section>

<section class="intro">
  <h2>HAVE A STORY TO TELL? WE CAN HELP YOU PUBLISH YOUR BOOK.</h2>
  <p>Welcome to Brellow Publishing , we are an independent publishing company located in London/Surrey. We publish Trade (fiction and non-fiction), &amp; Young Adult (YA) in a variety of subjects.</p>
  <div class="feature-row">
    <div class="feature" style="left:223px">
      <div class="feature-icon red">
        <svg width="86" height="86" viewBox="0 0 86 86" aria-hidden="true"><rect x="10" y="20" width="14" height="52" rx="2" fill="#5b3a2a"/><rect x="24" y="16" width="12" height="56" rx="2" fill="#2f7a3a"/><rect x="36" y="12" width="38" height="62" rx="3" fill="#1f8be0"/><rect x="36" y="12" width="8" height="62" fill="#176bb0"/></svg>
      </div><h3>BOOKS</h3></div>
    <div class="feature" style="left:475px">
      <div class="feature-icon blue">
        <svg width="90" height="80" viewBox="0 0 90 80" aria-hidden="true"><path d="M8 14 L44 20 L44 70 L8 64 Z M82 14 L46 20 L46 70 L82 64 Z" fill="none" stroke="#fff" stroke-width="7" stroke-linejoin="round"/></svg>
      </div><h3>AUTHORS</h3></div>
    <div class="feature" style="left:723px">
      <div class="feature-icon red">
        <svg width="84" height="84" viewBox="0 0 84 84" aria-hidden="true"><rect x="10" y="10" width="64" height="64" rx="8" fill="#1e6fc8"/><rect x="16" y="16" width="52" height="44" rx="4" fill="#2a86e6"/><path d="M26 38 L38 50 L60 26" fill="none" stroke="#12315e" stroke-width="7" stroke-linecap="round" stroke-linejoin="round"/></svg>
      </div><h3>SUBMISSIONS</h3></div>
  </div>
</section>

<section class="video-band" role="img" aria-label="Blurred photo of book pages and covers">
  <h2>LEARN HOW WE PUBLISH BOOKS</h2>
  <svg class="play" width="46" height="46" viewBox="0 0 46 46"><circle cx="23" cy="23" r="20" fill="none" stroke="#fff" stroke-width="4"/><path d="M18 13 L32 23 L18 33 Z" fill="#fff"/></svg>
</section>

<section class="steps">
  <h2 class="section-title">PUBLISH YOUR BOOK IN 4 EASY STEPS</h2>
  <div class="step" style="left:150px;top:152px">
    <svg width="110" height="100" viewBox="0 0 110 100"><polygon points="28,2 82,2 108,50 82,98 28,98 2,50" fill="#fff" stroke="var(--blue)" stroke-width="2"/><rect x="42" y="36" width="24" height="24" rx="3" fill="none" stroke="var(--red)" stroke-width="3"/><path d="M52 52 L70 32 L74 36 L56 56 Z" fill="var(--red)"/></svg>
    <h3>WRITING</h3>
    <p>You write a book to the best of your ability And after redrafting several times when you honestly feel that you have done the best you Possibly can with it, you send it to us</p>
  </div>
  <div class="step" style="left:610px;top:152px">
    <svg width="110" height="100" viewBox="0 0 110 100"><polygon points="28,2 82,2 108,50 82,98 28,98 2,50" fill="#fff" stroke="var(--blue)" stroke-width="2"/><rect x="42" y="34" width="26" height="32" rx="3" fill="none" stroke="var(--red)" stroke-width="3"/><path d="M47 42h4M55 42h9M47 50h4M55 50h9M47 58h4M55 58h9" stroke="var(--red)" stroke-width="2.5"/></svg>
    <h3>SUBMISSION</h3>
    <p>If your book is in our subject matter and you think you have something that could tickle our fancy, send Us your book for review.</p>
  </div>
  <div class="step" style="left:150px;top:396px">
    <svg width="110" height="100" viewBox="0 0 110 100"><polygon points="28,2 82,2 108,50 82,98 28,98 2,50" fill="#fff" stroke="var(--blue)" stroke-width="2"/><path d="M55 34 L60 46 L73 46 L63 54 L67 67 L55 59 L43 67 L47 54 L37 46 L50 46 Z" fill="var(--red)"/></svg>
    <h3>REVIEW</h3>
    <p>You send us your book and our editorial team<br>will look over it and decide if we like it and</p>
  </div>
  <div class="step" style="left:610px;top:396px">
    <svg width="110" height="100" viewBox="0 0 110 100"><polygon points="28,2 82,2 108,50 82,98 28,98 2,50" fill="#fff" stroke="var(--blue)" stroke-width="2"/><path d="M44 32 H60 L68 40 V68 H44 Z" fill="none" stroke="var(--red)" stroke-width="2.5"/><path d="M49 46h12M49 52h8" stroke="var(--red)" stroke-width="2"/><circle cx="59" cy="60" r="4" fill="none" stroke="var(--red)" stroke-width="2"/></svg>
    <h3>CONTRACT</h3>
    <p>You send us your book and our editorial team will look over it and decide if we like it and then we will Decide what</p>
  </div>
</section>

<section class="partners">
  <h2 class="section-title">COMPANIES WE WORK WITH</h2>
  <div class="partner-row">
    <span class="partner-badge flat" style="height:40px;--tone:#3a3a3a"></span>
    <span class="partner-badge" style="height:70px;--tone:#5fb7c9"></span>
    <span class="partner-badge flat" style="height:64px;--tone:#3d7fc4"></span>
    <span class="partner-badge" style="height:50px;--tone:#f08a2a"></span>
    <span class="partner-badge" style="height:74px;--tone:#2f5e3a"></span>
    <span class="partner-badge flat" style="height:48px;--tone:#7bbf4a"></span>
  </div>
</section>

<section class="testimonials">
  <h2 class="section-title">TESTIMONIALS</h2>
  <div class="quote-mark"><span>“</span></div>
  <div class="avatar" role="img" aria-label="Portrait photo of a client"></div>
  <p>You send us your book and our editorial team will look over it and decide<br>if we like it and then we will Decide what.</p>
</section>

<footer class="site-footer">
  <div class="footer-brand"><div class="brand-dot"></div><div class="brand-name">Brellow<br>Publishing</div></div>
  <div class="footer-col" style="left:300px"><h4>LINKS</h4><ul><li>Submissions</li><li>Production</li><li>Ebooks</li></ul></div>
  <div class="footer-col" style="left:490px"><h4>SERVICES</h4><ul><li>Books</li><li>Seminars</li><li>Packages</li></ul></div>
  <div class="footer-col" style="left:672px"><h4>OTHERS</h4><ul><li>Authors</li><li>Contact</li><li>Careers</li></ul></div>
  <div class="footer-col" style="left:836px"><h4>FOLLOW US</h4><div class="social"><span></span><span></span><span></span><span></span></div></div>
  <div class="footer-rule"></div>
  <p class="copyright">@copyright 2016 Brellowpublishing.All Rights Reserved.</p>
</footer>
</body>
</html>
```